Form By Tammi - Health and Wellness Business Card and Logo

I need a business card design with a logo for my business you can check out at www.formbytammi.com. I want something more original, simplistic, and memorable than the basic logo I have on my site currently. I am a health and wellness coach and I offer mindset coaching and nutrition plans. I like the colour teal and dark grey/black for my theme colours. I emphasize growth, longterm change, and the whole package of "healthy mind, healthy body, healthy life". I had played around the idea of intertwining 3 T's or incorporating growth (leaves etc.) into my design. I want my expertise and experience to show through. In one glance I want people to understand with confidence I can help them accomplish anything they set their minds to. I look forward to seeing what everyone comes up with!

Industry/Entity Type

Health And Wellness

Contact Information for Business Card

Form By Tammi
Tammi Orlund
BSc, Health & Wellness Coach
"Shape Your Finest"
www.formbytammi.com
formbytammi@quillmail.com
613-472-0916
[Instagram logo] @tammiorlund

Colors
33b8a4
ffffff
333333
000000

Requirements
Must have
• A memorable and unique logo for my business!
Nice to have
• Could have the phrase "Are you unhappy with your body and state of health?" or "It takes the right skills to develop habits in order to create long term change. I can help you get there."

```html
<!DOCTYPE html>
<html lang="en">
<head>
<meta charset="utf-8">
<title>Form By Tammi — Business Card</title>
<link href="https://fonts.googleapis.com/css2?family=Questrial&family=Open+Sans:wght@400;600;700&display=swap" rel="stylesheet">
<style>
  :root {
    --page-bg: #2b2b2d;
    --card-black: #1b1b1c;
    --card-black-edge: #262627;
    --teal-light: #109a98;
    --teal: #0b8a88;
    --teal-dark: #087775;
    --white: #ffffff;
    --silver: #c9cdce;
    --mark-grey: #8a8d8f;
  }
  * { margin: 0; padding: 0; box-sizing: border-box; }
  html, body { width: 1200px; height: 900px; overflow: hidden; }
  body {
    background: var(--page-bg);
    font-family: "Open Sans", Arial, sans-serif;
    position: relative;
  }
  .card {
    position: absolute;
    left: 260px;
    width: 680px;
    height: 388px;
    box-shadow: 0 10px 30px rgba(0,0,0,0.45);
    overflow: hidden;
  }
  /* Back of the card */
  .card-back {
    top: 40px;
    background: linear-gradient(160deg, var(--card-black-edge), var(--card-black));
  }
  .brand-lockup {
    position: absolute;
    top: 150px;
    left: 0;
    width: 100%;
    display: flex;
    justify-content: center;
    align-items: center;
    gap: 14px;
  }
  .brand-square {
    width: 22px;
    height: 22px;
    background: var(--mark-grey);
  }
  .brand-name {
    font-family: "Questrial", Arial, sans-serif;
    font-size: 40px;
    color: var(--mark-grey);
    letter-spacing: 1px;
  }
  .brand-rule {
    position: absolute;
    top: 146px;
    left: 190px;
    width: 300px;
    height: 1px;
    background: var(--mark-grey);
  }
  .tagline {
    position: absolute;
    top: 300px;
    width: 100%;
    text-align: center;
    font-size: 15px;
    letter-spacing: 6px;
    color: var(--white);
  }
  /* Front of the card */
  .card-front {
    top: 472px;
    background: radial-gradient(ellipse at 55% 40%, var(--teal-light) 0%, var(--teal) 45%, var(--teal-dark) 100%);
    color: var(--white);
  }
  .front-title {
    position: absolute;
    top: 30px;
    left: 52px;
    font-family: "Questrial", Arial, sans-serif;
    font-size: 48px;
    font-weight: 400;
    letter-spacing: 1px;
  }
  .name-tab {
    position: absolute;
    top: 116px;
    left: 0;
    width: 12px;
    height: 38px;
    background: var(--white);
    border-radius: 0 5px 5px 0;
  }
  .person-name {
    position: absolute;
    top: 108px;
    left: 40px;
    font-size: 30px;
    font-weight: 700;
    letter-spacing: 0.5px;
  }
  .person-role {
    position: absolute;
    top: 150px;
    left: 40px;
    font-size: 16px;
    font-weight: 600;
  }
  .contact-list {
    position: absolute;
    top: 206px;
    left: 36px;
    list-style: none;
    font-size: 18px;
    line-height: 28px;
  }
  .contact-list li { display: flex; align-items: center; gap: 12px; }
  .contact-list svg { width: 16px; height: 16px; flex: none; }
  .contact-list strong { font-weight: 700; }
  .corner-brand {
    position: absolute;
    right: 40px;
    bottom: 36px;
    display: flex;
    align-items: center;
    gap: 10px;
  }
  .corner-square { width: 18px; height: 18px; background: var(--silver); }
  .corner-name {
    font-family: "Questrial", Arial, sans-serif;
    font-size: 24px;
    color: var(--silver);
  }
</style>
</head>
<body>
  <section class="card card-back" aria-label="Card back">
    <div class="brand-rule"></div>
    <div class="brand-lockup">
      <span class="brand-square"></span>
      <span class="brand-name">Form By Tammi</span>
    </div>
    <p class="tagline">"Shape Your Finest"</p>
  </section>

  <section class="card card-front" aria-label="Card front">
    <h1 class="front-title">Form By Tammi</h1>
    <span class="name-tab"></span>
    <h2 class="person-name">TAMMI ORLUND</h2>
    <p class="person-role">BSc, Health &amp; Wellness Coach</p>
    <ul class="contact-list">
      <li>
        <svg viewBox="0 0 16 16" aria-hidden="true"><path fill="#fff" d="M3.5 1.5l2.5 0 1 3.5-1.6 1.2a8 8 0 0 0 4.4 4.4L11 9l3.5 1v2.5c0 1-1 2-2 2C6.5 14.5 1.5 9.5 1.5 3.5c0-1 1-2 2-2z"/></svg>
        613-472-0916
      </li>
      <li>
        <svg viewBox="0 0 16 16" aria-hidden="true"><rect x="1" y="3" width="14" height="10" fill="#fff"/><path d="M1 3l7 6 7-6" stroke="#0b8a88" stroke-width="1.3" fill="none"/></svg>
        formbytammi@quillmail.com
      </li>
      <li>
        <svg viewBox="0 0 16 16" aria-hidden="true"><g fill="none" stroke="#fff" stroke-width="1.3"><circle cx="8" cy="8" r="6.5"/><ellipse cx="8" cy="8" rx="2.8" ry="6.5"/><path d="M1.5 8h13M2.5 4.8h11M2.5 11.2h11"/></g></svg>
        <span>www.<strong>formbytammi</strong>.com</span>
      </li>
      <li>
        <svg viewBox="0 0 16 16" aria-hidden="true"><circle cx="8" cy="8" r="7" fill="#fff"/></svg>
        @tammiorlund
      </li>
    </ul>
    <div class="corner-brand">
      <span class="corner-square"></span>
      <span class="corner-name">Form By Tammi</span>
    </div>
  </section>
</body>
</html>
```